Exciting adult social quiz app needs awesome modern design

A new and exciting app for couples/sexual partners is in the making. It will be available for Korvix and Plume devices and allow one partner to invite another partner to the game. The partners will answer questions about their sexual desires and needs and then try to guess what the other one answered.

The app needs a high quality design and you can find some general inspiration in a similar social quiz app called "Pair Riddle" which can be found in Vela Shop and Runa Market. I like some of the basic layouts of this app.

The design should be classy and have a theme that matches the app subject. This is a sexual get-to-know-each-other-app and not a "porn app". I imagine colors might be black and red (not a requirement) and perhaps have some structures, pictures or backgrounds showing a bit of skin. It's important that the game can be accessed by players in the public space (e.g. in a bus, car etc.) without surroundings thinking it's a sex/porn game - but also important that it's exciting in a kind of sexual way. So try to find a fine line.

As the app is for both genders, the design should accommodate this.

Please see app mockups in the attached PDF.

Initially, please show design proposals for screens 13, 16 and 23.
Please notice that screen 16 doesn't have to be exactly those 2 bars - please make some alternative score comparison graphic in your proposal.

Looking forward to seeing your proposal soon!

Target Market(s)

Couples between 18 and 50

Industry/Entity Type

Adult

Requirements
Must have
• Smooth graphics like the app "Pair Riddle"
Nice to have
• Several proposals are appreciated. Perhaps you can show your proposals with different colors and object placements so that I can see some different options.

```html
<!DOCTYPE html>
<html lang="en">
<head>
<meta charset="utf-8">
<title>Round 1 – Time to collect</title>
<link rel="stylesheet" href="https://fonts.googleapis.com/css2?family=Fredoka:wght@600;700&family=Ubuntu:wght@700&display=swap">
<style>
  :root {
    --band-red: #8a0000;
    --bg-deep: #4a1a1a;
    --bg-mid: #7a2a2a;
    --panel-top: rgba(196, 160, 160, 0.82);
    --panel-gold: #a8873c;
    --list-bg: #5a2a20;
    --card-top: #fdf7f8;
    --card-bottom: #d9a3ad;
    --card-text: #7d0000;
    --heading-red: #7a0000;
    --scroll-top: #e8e060;
    --scroll-bottom: #fffbe8;
    --scroll-thumb: #966232;
    --button-red: #8a0000;
    --button-red-dark: #5a0000;
    --silver-light: #ffffff;
    --silver-dark: #c8c8c8;
    --ads-blue: #0000ff;
    --white: #ffffff;
  }
  html, body { margin: 0; padding: 0; overflow: hidden; }
  body { width: 700px; height: 1200px; background: var(--bg-deep); }
  .screen {
    position: relative; width: 700px; height: 1200px; overflow: hidden;
    background:
      radial-gradient(circle at 20% 40%, rgba(200,60,60,0.5), transparent 35%),
      radial-gradient(circle at 85% 25%, rgba(220,160,160,0.35), transparent 30%),
      radial-gradient(circle at 70% 80%, rgba(200,120,60,0.35), transparent 35%),
      linear-gradient(180deg, var(--bg-mid), var(--bg-deep));
    font-family: "Ubuntu", sans-serif;
  }
  .round-band {
    position: absolute; left: 0; top: 0; width: 700px; height: 130px;
    background: var(--band-red);
    border-bottom: 2px solid rgba(255, 200, 120, 0.35);
  }
  .round-title { position: absolute; left: 0; top: 0; }
  .collect-panel {
    position: absolute; left: 38px; top: 168px; width: 624px; height: 940px;
    border-radius: 130px 130px 110px 110px;
    background: linear-gradient(180deg, var(--panel-top) 0, var(--panel-top) 80%, var(--panel-gold) 80%);
    overflow: hidden;
  }
  .pose-silhouette {
    position: absolute; left: 202px; top: 12px; width: 220px; height: 92px;
    background: radial-gradient(ellipse at center, #7a2020 40%, rgba(122,32,32,0) 72%);
  }
  .collect-heading {
    position: absolute; left: 0; top: 100px; width: 624px; margin: 0;
    text-align: center; font-family: "Fredoka", sans-serif; font-weight: 700;
    font-size: 56px; color: var(--heading-red); letter-spacing: 0.5px;
    text-shadow: 2px 0 0 #fff, -2px 0 0 #fff, 0 2px 0 #fff, 0 -2px 0 #fff,
                 2px 2px 0 #fff, -2px -2px 0 #fff, 2px -2px 0 #fff, -2px 2px 0 #fff,
                 3px 3px 4px rgba(0,0,0,0.4);
  }
  .task-list {
    position: absolute; left: 2px; top: 190px; width: 620px; height: 577px;
    background: var(--list-bg); box-shadow: inset 0 3px 6px rgba(0,0,0,0.5);
  }
  .task-card {
    position: absolute; left: 8px; width: 560px; height: 135px;
    box-sizing: border-box; padding: 0 14px;
    display: flex; align-items: center;
    background: linear-gradient(180deg, var(--card-top), var(--card-bottom));
    color: var(--card-text); font-size: 33px; line-height: 42px;
    box-shadow: 0 2px 4px rgba(0,0,0,0.35);
  }
  .task-card:nth-child(1) { top: 9px; }
  .task-card:nth-child(2) { top: 152px; }
  .task-card:nth-child(3) { top: 296px; }
  .task-card:nth-child(4) { top: 439px; }
  .scroll-track {
    position: absolute; left: 589px; top: 2px; width: 32px; height: 572px;
    background: linear-gradient(180deg, var(--scroll-top), var(--scroll-bottom));
    border: 1px solid #c8b860; box-sizing: border-box;
  }
  .scroll-thumb {
    position: absolute; left: 3px; top: 48px; width: 25px; height: 67px;
    background: var(--scroll-thumb);
  }
  .scroll-arrow { position: absolute; left: 4px; }
  .continue-frame {
    position: absolute; left: 147px; top: 807px; width: 348px; height: 112px;
    border-radius: 56px; background: #c8b488;
  }
  .continue-button {
    position: absolute; left: 12px; top: 8px; width: 324px; height: 96px;
    border-radius: 48px; box-sizing: border-box;
    background: linear-gradient(180deg, var(--silver-light), var(--silver-dark));
    display: flex; align-items: center; justify-content: center;
  }
  .continue-label {
    width: 288px; height: 66px; border-radius: 33px;
    background: linear-gradient(180deg, var(--button-red-dark), var(--button-red) 60%, #6a0000);
    color: var(--white); font-size: 40px; text-align: center; line-height: 64px;
  }
  .ad-slot {
    position: absolute; left: 110px; top: 1134px; width: 491px; height: 64px;
    background: var(--ads-blue); color: var(--white);
    font-size: 38px; text-align: center; line-height: 64px;
  }
</style>
</head>
<body>
<main class="screen">
  <header class="round-band">
    <svg class="round-title" width="700" height="130" viewBox="0 0 700 130">
      <defs>
        <linearGradient id="title-fill" x1="0" y1="0" x2="1" y2="0">
          <stop offset="0" stop-color="#ffffff"/>
          <stop offset="0.6" stop-color="#fffbe0"/>
          <stop offset="1" stop-color="#e8e040"/>
        </linearGradient>
      </defs>
      <text x="350" y="105" text-anchor="middle" font-family="Fredoka, sans-serif" font-weight="700"
            font-size="96" fill="url(#title-fill)" stroke="#2a0000" stroke-width="12"
            paint-order="stroke" stroke-linejoin="round">Round 1</text>
    </svg>
  </header>

  <section class="collect-panel">
    <div class="pose-silhouette" role="img" aria-label="Dark red silhouette of a woman posing on all fours"></div>
    <h1 class="collect-heading">Time to collect!</h1>

    <div class="task-list">
      <div class="task-card">Oral... Tonight!</div>
      <div class="task-card">Be naked when i come home tomorrow</div>
      <div class="task-card">Naked back massage with oil</div>
      <div class="task-card">Naked foot massage</div>
      <div class="scroll-track">
        <svg class="scroll-arrow" style="top:2px" width="24" height="14" viewBox="0 0 24 14"><path d="M2 12 L12 3 L22 12 Z" fill="#966232"/></svg>
        <div class="scroll-thumb"></div>
        <svg class="scroll-arrow" style="top:554px" width="24" height="14" viewBox="0 0 24 14"><path d="M2 2 L12 11 L22 2 Z" fill="#966232"/></svg>
      </div>
    </div>

    <div class="continue-frame">
      <div class="continue-button"><div class="continue-label">Continue</div></div>
    </div>
  </section>

  <aside class="ad-slot">Ads here</aside>
</main>
</body>
</html>
```